Veteran Reserved Parking Sign 12x18

Brave Hearts Kinship Network is looking to have a new Veteran Reserved Parking Sign designed. Included in the files are our current logo, the rectangle with the name on it. Also included is our Alt Square version that we will often use. There are several other signs that we kind of like as examples, not not asking for exactly like those, we want you to be creative and show us some new ideas. These are full sized parking signs, 12" wide X 18" height.

Target Market(s)

Veterans and Military Friendly Americans

Industry/Entity Type

Veteran Nonprofit

Font styles to use
Other font styles liked:
• Our logo uses the Franklin Heavy Gothic Font but you are not required to use that font in design.

Requirements
Must have
• Our logo needs to be on there and well as BHKN.ORG
Should not have
• CAN NOT Mention Steadfast Soldier Alliance or have black silhouettes similar to their logo. BHKN is NOT the same nonprofit.

```html
<!DOCTYPE html>
<html lang="en">
<head>
<meta charset="utf-8">
<title>Reserved Veteran Parking Sign – Brave Hearts Kinship Network</title>
<link rel="stylesheet" href="https://fonts.googleapis.com/css2?family=Oswald:wght@500;600&family=Montserrat:wght@600;700&display=swap">
<style>
  :root {
    --sign-red: #d62a3b;
    --sign-navy: #224a85;
    --sign-sky: #00a0e3;
    --sign-white: #ffffff;
    --page-bg: #ffffff;
  }
  html, body {
    margin: 0;
    padding: 0;
    width: 1200px;
    height: 1200px;
    overflow: hidden;
    background: var(--page-bg);
  }
  .canvas {
    position: relative;
    width: 1200px;
    height: 1200px;
  }
  .parking-sign {
    position: absolute;
    left: 0;
    top: 0;
    width: 1200px;
    height: 1200px;
  }
  .sign-heading {
    font-family: "Oswald", "Arial Narrow", sans-serif;
    font-weight: 600;
  }
  .heading-reserved { fill: var(--sign-white); }
  .heading-veteran { fill: var(--sign-sky); }
  .heading-parking { fill: var(--sign-white); font-weight: 500; }
  .thanks-line {
    font-family: "Montserrat", Arial, sans-serif;
    font-weight: 600;
    font-size: 13.5px;
    letter-spacing: 1.7px;
    fill: var(--sign-white);
  }
  .org-name {
    font-family: "Montserrat", Arial, sans-serif;
    font-weight: 700;
    font-size: 17px;
    fill: var(--sign-navy);
  }
</style>
</head>
<body>
<main class="canvas">
  <svg class="parking-sign" viewBox="0 0 1200 1200" xmlns="http://www.w3.org/2000/svg" aria-label="Reserved veteran parking sign">
    <defs>
      <clipPath id="panel-clip">
        <rect x="414" y="282" width="370" height="576" rx="40" ry="40"/>
      </clipPath>
      <clipPath id="frame-clip">
        <rect x="398" y="268" width="402" height="604" rx="54" ry="54"/>
      </clipPath>
      <path id="thanks-arc" d="M 462 760 Q 598 710 736 760"/>
    </defs>

    <rect class="sign-frame" x="398" y="268" width="402" height="604" rx="54" ry="54" fill="var(--sign-red)"/>

    <g class="sign-panel" clip-path="url(#panel-clip)">
      <rect x="414" y="282" width="370" height="576" fill="var(--sign-navy)"/>
      <polygon points="414,282 452,282 598,328 745,282 784,282 784,270 414,270" fill="var(--sign-red)"/>
      <path d="M 398 805 Q 598 691 800 805 L 800 870 L 398 870 Z" fill="var(--sign-sky)"/>
      <path d="M 398 813 Q 598 703 800 813 L 800 870 L 398 870 Z" fill="var(--sign-white)"/>
    </g>

    <g class="parking-banner" clip-path="url(#frame-clip)">
      <polygon points="398,578 598,546 800,578 800,590 598,558 398,590" fill="var(--sign-sky)"/>
      <polygon points="398,590 598,558 800,590 800,672 598,702 398,672" fill="var(--sign-red)"/>
      <polygon points="398,672 598,702 800,672 800,682 598,714 398,682" fill="var(--sign-sky)"/>
    </g>

    <text class="sign-heading heading-reserved" x="443" y="432" font-size="88" textLength="310" lengthAdjust="spacingAndGlyphs">RESERVED</text>
    <text class="sign-heading heading-veteran" x="443" y="532" font-size="93" textLength="310" lengthAdjust="spacingAndGlyphs">VETERAN</text>
    <text class="sign-heading heading-parking" x="443" y="662" font-size="88" textLength="310" lengthAdjust="spacingAndGlyphs">PARKING</text>

    <text class="thanks-line">
      <textPath href="#thanks-arc" startOffset="50%" text-anchor="middle">THANK YOU FOR YOUR SERVICE</textPath>
    </text>

    <text class="org-name" x="598" y="818" text-anchor="middle">Brave Hearts Kinship Network</text>
  </svg>
</main>
</body>
</html>
```